New York Property Management Company needs a Brochure Designed

We need a brochure for a new property management company in New York called KT7 Realty Partners. The 2 is superscript (squared.) We are looking for buildings to manage and want to showcase our expertise and caring. Logo is attached. We are getting a different photo and do not need all the verbiage. Also, does not need to be a trifold.
Updates

Property management group is a RESIDENTIAL property management group. I neglected to mention that. Thanks.

Hi designers, We've received very few designs so far so we've extended the deadline. We're hoping to receive your creative submissions soon! Thank you!

Reason: A few people have to weigh in on the design and it has been difficult coordinating this. We are getting close to making a decision and just need a few more days.

Industry/Entity Type

Property Management

```html
<!DOCTYPE html>
<html lang="en">
<head>
<meta charset="utf-8">
<title>KT7 Realty Partners – Leadership</title>
<link href="https://fonts.googleapis.com/css2?family=Montserrat:wght@300;600&family=Source+Sans+3:wght@400&display=swap" rel="stylesheet">
<style>
  :root {
    --panel: #2e2826;
    --ink-light: #ffffff;
    --body-light: #f1eeec;
    --paper: #ffffff;
    --mist: #e4e6e8;
    --steel-dark: #4f5a60;
    --steel-light: #e6e9ea;
  }
  html, body {
    margin: 0;
    padding: 0;
    width: 1200px;
    height: 1200px;
    overflow: hidden;
    background: var(--paper);
  }
  .sheet {
    position: relative;
    width: 1200px;
    height: 1200px;
    overflow: hidden;
    background: var(--paper);
    font-family: "Source Sans 3", "Myriad Pro", Arial, sans-serif;
  }
  .edge-fade {
    position: absolute;
    left: 0; top: 0;
    width: 110px; height: 730px;
    background: linear-gradient(90deg, var(--mist), var(--paper));
  }
  .team-photo {
    position: absolute;
    left: 110px; top: 0;
    width: 500px; height: 730px;
    background:
      linear-gradient(180deg, #b9b0a6 0%, #8e8178 30%, #7b7774 55%, #5a5552 72%, #b7aea2 86%, #d8d0c4 100%);
  }
  .panel-top {
    position: absolute;
    left: 610px; top: 0;
    width: 590px; height: 730px;
    background: var(--panel);
  }
  .panel-bottom {
    position: absolute;
    left: 180px; top: 730px;
    width: 1020px; height: 373px;
    background: var(--panel);
  }
  .side-strip {
    position: absolute;
    left: 0; top: 730px;
    width: 180px; height: 373px;
    background: linear-gradient(90deg, #d5d8da, #f3f4f5);
  }
  .footer-band {
    position: absolute;
    left: 0; top: 1103px;
    width: 1200px; height: 97px;
    background: linear-gradient(90deg, var(--steel-dark) 0%, var(--steel-light) 45%, var(--steel-light) 55%, var(--steel-dark) 100%);
  }
  .bio-name {
    position: absolute;
    margin: 0;
    font-family: "Montserrat", "Century Gothic", sans-serif;
    font-weight: 300;
    font-size: 40px;
    line-height: 1;
    color: var(--ink-light);
    letter-spacing: 0.2px;
  }
  .bio-name strong { font-weight: 600; }
  .bio-text {
    position: absolute;
    color: var(--body-light);
  }
  .bio-text p { margin: 0 0 20px; }
  .bio-lead .bio-name { left: 626px; top: 116px; }
  .bio-lead .bio-text {
    left: 628px; top: 178px;
    width: 556px;
    font-size: 15px;
    line-height: 20px;
  }
  .bio-partner .bio-name { left: 626px; top: 690px; }
  .bio-partner .bio-text {
    left: 194px; top: 742px;
    width: 990px;
    font-size: 14.5px;
    line-height: 19.5px;
  }
  .bio-partner .bio-text p { margin-bottom: 19px; }
</style>
</head>
<body>
<main class="sheet">
  <div class="edge-fade"></div>
  <div class="team-photo" role="img" aria-label="Photo of the two founding partners standing on a city rooftop terrace"></div>
  <div class="panel-top"></div>
  <div class="side-strip"></div>
  <div class="panel-bottom"></div>
  <div class="footer-band"></div>

  <section class="bio bio-lead">
    <h2 class="bio-name">Martin <strong>Keller</strong></h2>
    <div class="bio-text">
      <p>Prior to co-founding KT7 Realty Partners, Martin was the Acquisitions Manager and a Senior Property Manager at Harborline Residential New York, LLC (formerly Bleecker Row Realty, Inc.) managing properties and locating investment opportunities for the principals of Harborline. Martin used his management, investment and development knowledge to create and implement asset repositioning plans including renovations and re-leasing for investments in order to maximize value for investors. Martin has managed over 1200 units in more than 30 buildings including residential and commercial owners/tenants and 50+ staff members.</p>
      <p>Martin has experience in high end and affordable housing including rent stabilized units in the rental, coop and condo markets both from Harborline and his prior position at The Okoro Group in Washington, DC. He began working in property management upon graduation from Chesapeake State University with a degree in Economics. Martin grew up in Minneapolis, MN.</p>
      <p>Martin established himself as a leading manager and key investment advisor at Harborline. He is an entrepreneur and is parlaying his unique skills and knowledge into making KT7 one of New York City's leading property management and real estate investment firms.</p>
    </div>
  </section>

  <section class="bio bio-partner">
    <h2 class="bio-name">Diane <strong>Talbot</strong></h2>
    <div class="bio-text">
      <p>Before co-founding KT7 Realty Partners, Diane was a Team Leader at Harborline Residential (formerly Bleecker Row), managing a team of 10+ managers responsible for a portfolio of multi-family buildings varying in size, location and prominence in Manhattan, Riverdale and Queens. She has been in property management for 12 years. She also served as Vice President of Client Accounting, utilizing her accounting background and management experience to restructure the department to better serve Bleecker Row clients.</p>
      <p>Diane has over 20 years of experience in various aspects of the management business. She was Board President of a large Westside Manhattan cooperative for more than 10 years. She began her career in New York at Meridian Card Services in finance, accounting and marketing positions. Her passion and interest in the management business prompted her to change careers and she joined a small management company in 2002. She rose through the ranks to both lead Client Accounting and her management team.</p>
      <p>Diane is originally from San Diego, California, where she obtained her Certified Public Accounting license while working for Pell &amp; Whitcombe. She moved to New York where she earned her Masters in Business Administration (finance) from Hudson Heights University. Her undergraduate degree is in accounting from Pacific Coast University.</p>
      <p>During Diane's tenure at Harborline/Bleecker Row, she established herself as a high performing manager and leader. Her broad scope of experience and education continue to be utilized by many buildings in improving financial performance, building operations and staff management. She is continuing to leverage these skills in building KT7RP.</p>
    </div>
  </section>
</main>
</body>
</html>
```